Kestrel Summit 2019 Enemies of the End-Times Church Flyer

We want a church conference flyer designed. We are looking for a professional, yet catchy design that uses our brand colors and logo creatively while communicating key information of the event effectively. <br/>The flyer must include all of the following:<br/>Title: Kestrel Summit 2019<br/>Topic: The Enemies of The End-Times Church <br/>Subtitles: <br/> -How the antichrist raises an army by social behavior engineering. <br/>-How the architects of modern social constructs escaped the church's radar. <br/>-The Holy Spirit's end-times agenda:<br/> The Knock-Out Punch!<br/>Speaker: Prophet Marcus Toliver <br/>Dates/time: December 27, 28 & 29 at 6pm<br/>Location: Halvorn Community Center <br/> 241 Pellham Street <br/> Portland, ME 04102<br/>Contact info: phone: 207-555-0148 <br/>email: contact@brookmeadow.example <br/> www.vutel.example<br/>*The flyer must also include a picture of the speaker and our Vutel logo <br/>Thanks, we look forward to seeing what you come up with!

Colors

Designer to choose colors to be used in the design.

Requirements
Must have
• The flyer must include all of the following:
• Title: Kestrel Summit 2019
• Topic: The Enemies of The End-Times Church
• Subtitles:
• -How the antichrist raises an army by social behavior engineering.
• -How the architects of modern social constructs escaped the church's radar.
• -The Holy Spirit's end-times agenda:
• The Knock-Out Punch!
• Speaker: Prophet Marcus Toliver
• Dates/time: December 27, 28 & 29 at 6pm
• Location: Halvorn Community Center
• 241 Pellham Street
• Portland, ME 04102
• Contact info: phone: 207-555-0148
• email: contact@brookmeadow.example
• www.vutel.example
• *The flyer must also include a picture of the speaker and our Vutel logo
Should not have
• Pictures of crosses or church buildings

```html
<!DOCTYPE html>
<html lang="en">
<head>
<meta charset="utf-8">
<title>Kestrel Summit 2019 Flyer</title>
<link rel="stylesheet" href="https://fonts.googleapis.com/css2?family=Playfair+Display:wght@400;900&family=Open+Sans:ital,wght@0,400;1,400&display=swap">
<style>
  :root {
    --ink: #111111;
    --paper: #ffffff;
    --band: #5b5b5b;
    --brand: #1d3b6e;
    --accent: #f2a12a;
    --photo-a: #6d6a66;
    --photo-b: #8a7a68;
    --photo-c: #a59a8c;
  }
  html, body {
    margin: 0;
    padding: 0;
    overflow: hidden;
    background: var(--paper);
  }
  .flyer {
    position: relative;
    width: 927px;
    height: 1200px;
    background: var(--paper);
    color: var(--ink);
    overflow: hidden;
    font-family: "Open Sans", Arial, sans-serif;
  }
  .brand {
    position: absolute;
    top: 42px;
    left: 0;
    width: 100%;
    display: flex;
    justify-content: center;
    align-items: center;
    gap: 12px;
  }
  .brand-dot {
    width: 22px;
    height: 22px;
    border-radius: 50%;
    background: var(--accent);
  }
  .brand-name {
    font-family: "Playfair Display", Georgia, serif;
    font-weight: 400;
    font-size: 46px;
    letter-spacing: 2px;
    color: var(--brand);
    text-transform: uppercase;
  }
  .rule {
    position: absolute;
    left: 31px;
    width: 873px;
    height: 15px;
    background: var(--ink);
  }
  .rule-top { top: 140px; }
  .rule-bottom { top: 369px; }
  .event-title {
    position: absolute;
    top: 160px;
    left: 0;
    width: 100%;
    margin: 0;
    text-align: center;
    font-family: "Playfair Display", Georgia, serif;
    font-weight: 900;
    font-size: 138px;
    line-height: 1;
    letter-spacing: 3px;
  }
  .event-subtitle {
    position: absolute;
    top: 320px;
    left: 0;
    width: 100%;
    text-align: center;
    font-size: 16px;
    letter-spacing: 2px;
    text-transform: uppercase;
  }
  .topic {
    position: absolute;
    top: 428px;
    left: 0;
    width: 100%;
    margin: 0;
    text-align: center;
    font-family: "Playfair Display", Georgia, serif;
    font-weight: 400;
    font-size: 31px;
  }
  .talks {
    position: absolute;
    top: 512px;
    left: 60px;
    width: 807px;
    margin: 0;
    padding: 0;
    list-style: none;
    text-align: center;
    font-size: 24px;
    line-height: 27px;
  }
  .talks li { margin-bottom: 22px; }
  .speaker-row {
    position: absolute;
    top: 772px;
    left: 33px;
    right: 33px;
    display: flex;
    justify-content: space-between;
    font-family: "Playfair Display", Georgia, serif;
    font-size: 24px;
  }
  .photo-band {
    position: absolute;
    top: 818px;
    left: 0;
    width: 100%;
    height: 213px;
    background: var(--band);
  }
  .photo {
    position: absolute;
    top: 22px;
    width: 174px;
    height: 171px;
  }
  .photo-1 { left: 58px; background: linear-gradient(160deg, var(--photo-a), #3e3b38); }
  .photo-2 { left: 374px; background: linear-gradient(160deg, var(--photo-b), #2f2a26); }
  .photo-3 { left: 647px; background: linear-gradient(160deg, var(--photo-c), #6a5c50); }
  .details {
    position: absolute;
    font-style: italic;
    font-size: 17px;
    line-height: 24px;
  }
  .location { top: 1095px; left: 73px; }
  .location .street { padding-left: 100px; }
  .contact { top: 1099px; left: 572px; }
  .website {
    top: 1160px;
    left: 0;
    width: 100%;
    text-align: center;
  }
</style>
</head>
<body>
<main class="flyer">
  <header class="brand">
    <span class="brand-dot"></span>
    <span class="brand-name">Vutel</span>
  </header>

  <div class="rule rule-top"></div>
  <h1 class="event-title">KESTREL</h1>
  <div class="event-subtitle">Summit&nbsp;&nbsp;2019</div>
  <div class="rule rule-bottom"></div>

  <h2 class="topic">The Enemies of the End - Times Church</h2>
  <ul class="talks">
    <li>How the antichrist raises an army by social behavior engineering</li>
    <li>How the architects of modern&nbsp; social constructs escaped the<br>church’s radar</li>
    <li>The Holy Spirit’s end-times agenda: The Knock-Out Punch!</li>
  </ul>

  <div class="speaker-row">
    <span class="speaker">Speaker: Prophet Marcus Toliver</span>
    <span class="dates">December 27, 28 &amp; 29 at 6pm</span>
  </div>

  <section class="photo-band">
    <div class="photo photo-1" role="img" aria-label="Photo of the speaker gesturing while seated at a desk"></div>
    <div class="photo photo-2" role="img" aria-label="Photo of the speaker in a suit before bookshelves"></div>
    <div class="photo photo-3" role="img" aria-label="Photo of the speaker smiling in a light shirt"></div>
  </section>

  <div class="details location">
    <div>LOCATION: Halvorn Community Center</div>
    <div class="street">241 Pellham Street Portland. ME 04102</div>
  </div>
  <div class="details contact">
    <div>CONTACT INFO: 207-555-0148</div>
    <div>EMAIL: contact@brookmeadow.example</div>
  </div>
  <div class="details website">WEBSITE: www.vutel.example</div>
</main>
</body>
</html>
```